The Brandwell Group Billboard Design

The Brandwell Group is doing a Roadster Raymond campaign and we need a billboard design. The following are the requirements:

1. We need Raymond Brandwell, who is in the photo attached, to be photoshopped into a black leather three-piece suit, white hair and beard, next to a really cool old school Torvin Kessler motorcycle, with a South Carolina scene in the background.
2. The Billboard should have the slogan "Motorcycle Wreck? We have your back!"
3. Our logo, which is attached, needs to be on the billboard
4. Our phone number needs to be on the billboard - (555) 214-6170
5. Torvin Kessler colors

```html
<!DOCTYPE html>
<html lang="en">
<head>
<meta charset="utf-8">
<title>The Brandwell Group — Motorcycle Wreck Billboard</title>
<link rel="stylesheet" href="https://fonts.googleapis.com/css2?family=Anton&family=Oswald:wght@500&display=swap">
<style>
  :root {
    --page-bg: #e9ecef;
    --sky-top: #0d1f4a;
    --sky-mid: #1d4f9c;
    --sky-light: #6fa6da;
    --sunset: #e88a2c;
    --sunset-glow: #f6b55a;
    --ground: #2a2418;
    --ground-light: #6b5a34;
    --chrome-dark: #121417;
    --chrome-mid: #3b4048;
    --suit: #15161a;
    --hair: #e6e2dc;
    --white: #ffffff;
    --brand-orange: #e97b26;
  }
  * { margin: 0; padding: 0; box-sizing: border-box; }
  html, body {
    width: 1200px;
    height: 895px;
    overflow: hidden;
    background: var(--page-bg);
  }
  .billboard {
    position: absolute;
    left: 50px;
    top: 170px;
    width: 1100px;
    height: 555px;
    overflow: hidden;
    font-family: "Anton", "Oswald", sans-serif;
    color: var(--white);
  }
  .scene-photo {
    position: absolute;
    inset: 0;
    background:
      linear-gradient(180deg, rgba(0,0,0,0) 55%, var(--ground-light) 66%, var(--ground) 100%),
      linear-gradient(90deg, var(--sky-top) 0%, rgba(13,31,74,0) 55%),
      linear-gradient(180deg, var(--sky-top) 0%, var(--sky-mid) 30%, var(--sky-light) 48%, var(--sunset-glow) 56%, var(--sunset) 62%, var(--ground) 70%);
  }
  .motorcycle-photo {
    position: absolute;
    left: 360px;
    top: 365px;
    width: 280px;
    height: 190px;
    border-radius: 46% 40% 0 0 / 55% 45% 0 0;
    background: linear-gradient(160deg, var(--chrome-mid) 0%, var(--chrome-dark) 60%, #050607 100%);
    opacity: 0.92;
  }
  .rider-photo {
    position: absolute;
    left: 650px;
    top: 165px;
    width: 210px;
    height: 390px;
    border-radius: 44% 44% 8px 8px / 22% 22% 0 0;
    background: linear-gradient(180deg, var(--hair) 0%, var(--hair) 22%, var(--suit) 30%, var(--suit) 100%);
  }
  .headline {
    position: absolute;
    left: 55px;
    top: 26px;
    text-transform: uppercase;
    letter-spacing: 0.5px;
    font-weight: 400;
  }
  .headline__lead {
    display: block;
    font-size: 50px;
    line-height: 1.05;
    margin-bottom: 4px;
  }
  .headline__main {
    display: block;
    font-size: 112px;
    line-height: 1.02;
  }
  .brand {
    position: absolute;
    left: 55px;
    bottom: 70px;
  }
  .brand__name {
    display: flex;
    align-items: center;
    gap: 10px;
    font-size: 44px;
    color: var(--brand-orange);
    letter-spacing: 1px;
    line-height: 1;
  }
  .brand__dot {
    width: 22px;
    height: 22px;
    border-radius: 50%;
    background: var(--brand-orange);
  }
  .brand__tagline {
    margin-top: 6px;
    font-family: "Oswald", sans-serif;
    font-weight: 500;
    font-size: 14px;
    letter-spacing: 0.6px;
    text-transform: uppercase;
    color: var(--brand-orange);
  }
  .phone {
    position: absolute;
    right: 36px;
    bottom: 22px;
    display: flex;
    align-items: center;
    gap: 10px;
    font-family: "Oswald", sans-serif;
    font-weight: 500;
    font-size: 26px;
  }
  .phone svg { width: 24px; height: 24px; }
</style>
</head>
<body>
  <main class="billboard">
    <div class="scene-photo" role="img" aria-label="South Carolina coastal landscape at sunset under a deep blue sky"></div>
    <div class="motorcycle-photo" role="img" aria-label="Black and chrome old school cruiser motorcycle"></div>
    <div class="rider-photo" role="img" aria-label="Raymond Brandwell with white hair and beard in a black leather three-piece suit"></div>

    <h1 class="headline">
      <span class="headline__lead">Motorcycle Wreck?</span>
      <span class="headline__main">We Have<br>Your Back!</span>
    </h1>

    <div class="brand">
      <div class="brand__name">BRANDWELL <span class="brand__dot"></span></div>
      <div class="brand__tagline">South Carolina Motorcycle Wreck Lawyers</div>
    </div>

    <div class="phone">
      <svg viewBox="0 0 24 24" aria-hidden="true">
        <circle cx="12" cy="12" r="12" fill="#ffffff"/>
        <path d="M8.2 6.2c.4-.4 1-.4 1.3 0l1.3 1.6c.3.4.3.9 0 1.2l-.8.8c.6 1.3 1.6 2.4 2.9 3l.8-.8c.3-.3.9-.4 1.2 0l1.6 1.3c.4.3.4.9 0 1.3l-.9.9c-.6.6-1.5.8-2.3.5-2.9-1.1-5.1-3.3-6.2-6.2-.3-.8-.1-1.7.5-2.3z" fill="#15161a"/>
      </svg>
      (555) 214-6170
    </div>
  </main>
</body>
</html>
```